New Innovative Counselling and psychotherapy Service needs Business Card design

Keep it simple and professional. On one side, just company name and logo (perhaps in all blue) and maybe a tag line.

On other side (all white) my name and Qualifications in centre

Industry/Entity Type

Health And Wellness

Contact Information for Business Card

Derek Hollis
Counsellor & Psychotherapist
BSc (Psychol.), BA, Dip. (Couns. & Psych.), PG.Cert (CBT), MGVrA, NWTF

I will also require Mobile no, Email and web site address of which I'll pass on to final designer.

Font styles to use
Sans Serif

Requirements
Must have
• My Logo Only and please use the colours in logo that is in it.
Should not have
• Any other images

```html
<!DOCTYPE html>
<html lang="en">
<head>
<meta charset="utf-8">
<title>Business Card – Counselling &amp; Psychotherapy</title>
<link rel="stylesheet" href="https://fonts.googleapis.com/css2?family=Montserrat:wght@300;400;700&display=swap">
<style>
  :root {
    --brand-blue: #4ab3ec;
    --paper: #ffffff;
    --canvas-bg: #ffffff;
  }
  html, body {
    margin: 0;
    padding: 0;
    width: 1200px;
    height: 1000px;
    overflow: hidden;
    background: var(--canvas-bg);
    font-family: "Montserrat", Arial, sans-serif;
  }
  .canvas {
    position: relative;
    width: 1200px;
    height: 1000px;
  }
  .card {
    position: absolute;
    left: 381px;
    width: 438px;
    box-sizing: border-box;
  }
  .card--front {
    top: 252px;
    height: 268px;
    background: var(--paper);
    border: 2px solid var(--brand-blue);
    color: var(--brand-blue);
    text-align: center;
  }
  .contact-block {
    position: absolute;
    left: 0;
    right: 0;
    top: 67px;
  }
  .holder-name {
    margin: 0;
    font-size: 17px;
    font-weight: 700;
    line-height: 22px;
  }
  .holder-role {
    margin: 0;
    font-size: 11.5px;
    font-weight: 700;
    line-height: 15px;
  }
  .holder-qualifications {
    margin: 1px 0 0;
    font-size: 12.5px;
    font-weight: 300;
    line-height: 15.5px;
  }
  .contact-lines {
    margin: 14px 0 0;
    font-size: 11.5px;
    font-weight: 700;
    line-height: 15.5px;
  }
  .card--back {
    top: 545px;
    height: 267px;
    background: var(--brand-blue);
  }
  .brand-lockup {
    position: absolute;
    left: 74px;
    top: 100px;
    display: flex;
    align-items: center;
    gap: 21px;
  }
  .brand-dot {
    width: 58px;
    height: 58px;
    display: block;
  }
  .brand-name {
    color: var(--paper);
    font-size: 27px;
    font-weight: 400;
    letter-spacing: -0.5px;
    white-space: nowrap;
  }
</style>
</head>
<body>
<main class="canvas">
  <section class="card card--front" aria-label="Card front">
    <div class="contact-block">
      <h1 class="holder-name">Derek Hollis</h1>
      <p class="holder-role">Counsellor &amp; Psychotherapist</p>
      <p class="holder-qualifications">BSc (Psychol.), BA, Dip. (Couns. &amp; Psych.),<br>PG.Cert (CBT), MGVrA, NWTF</p>
      <p class="contact-lines">M: 123 4567<br>youremail@mailbox.com<br>www. websiteaddress</p>
    </div>
  </section>

  <section class="card card--back" aria-label="Card back">
    <div class="brand-lockup">
      <svg class="brand-dot" viewBox="0 0 58 58" aria-hidden="true">
        <circle cx="29" cy="29" r="29" fill="var(--paper)"/>
      </svg>
      <span class="brand-name">Clearwater Lane</span>
    </div>
  </section>
</main>
</body>
</html>
```